Wordpress Design Project

TWEE STILLE WERVEN translates to English as 'GOOD BUSINESS'. We have started a new social innovation project that aims to get more people to fully participate in regular societal 'live'. Many people stay behind of stand aside our economic and social developments, due to a lack of education, lack of motivation, lack of opportunities, because the global changes have simply moved too fast for them, or because of a lack of understanding what each individual can truly contribute. We want to change that. To achieve this we will help individuals discover their personal creative talents. Not, as is the case, by forcing those people to come a central location such as social institutes or schools, but by actually visiting them in their livelihood with our new 'Roving Atelier'. By using the latest Gaming-insights and a highly entertaining creative program, we expect to motivate everybody to challenge themselves. Based on personal insights and regained interests in opportunities we will guide them in building self confidence, a new network, and basic craftmanship that will allow everybody to apply for quality work! As, and that takes us back to the foundation of 'TWEE STILLE WREVEN', we believe that social and economic values go hand in hand.

Target Market(s)

CORPORATIONS, GOVERNMENT AGENCIES

Industry/Entity Type

Building

Requirements
Must have
• Structure:
PAGES: HOME, TWEE STILLE WERVEN, ACTIVITIES, ABOUT US, CONTACT, BLOG

POST CATEGORIES: JOIN US, BACKGROUND INFO, UPDATES, ACTIVITIES, CV, BLOG
Nice to have
• PICTURE SLIDES ON HOME PAGE

POSTS WITH STRONG VISUAL CONTENT

PORTFOLIO DESIGNS FOR POST DISPLAYS

```html
<!DOCTYPE html>
<html lang="en">
<head>
<meta charset="utf-8">
<title>Twee Stille Werven — Blog</title>
<link rel="stylesheet" href="https://fonts.googleapis.com/css2?family=Source+Sans+3:wght@300;400;600&display=swap">
<style>
  :root {
    --header-bg: #1e0a22;
    --page-bg: #222222;
    --accent: #6e2540;
    --date-tile: #c0838f;
    --date-text: #ffffff;
    --heading-text: #e8e8e8;
    --card-bg: #e1e1e1;
    --card-text: #3a3a3a;
    --card-border: #c0838f;
    --link: #7a2446;
    --load-bg: #0b0b0b;
    --load-text: #e8e8e8;
    --row-gap: #121212;
  }
  * { margin: 0; padding: 0; box-sizing: border-box; }
  html, body { width: 1173px; height: 1200px; overflow: hidden; }
  body {
    position: relative;
    background: var(--page-bg);
    font-family: "Source Sans 3", "Myriad Pro", sans-serif;
    color: var(--heading-text);
  }

  /* Header */
  .site-header {
    position: absolute; left: 0; top: 0; width: 1173px; height: 73px;
    background: var(--header-bg);
  }
  .site-name {
    position: absolute; left: 100px; top: 18px;
    font-size: 26px; font-weight: 600; letter-spacing: 0.5px; color: #ffffff;
    white-space: nowrap;
  }
  .main-nav {
    position: absolute; left: 385px; top: 25px;
    display: flex; gap: 11px;
    font-size: 14.5px; font-weight: 400; color: #ffffff;
    list-style: none; white-space: nowrap;
  }
  .header-button {
    position: absolute; top: 0; width: 73px; height: 73px;
    background: var(--accent);
    display: flex; align-items: center; justify-content: center;
  }
  .header-button--top { left: 868px; }
  .header-button--add { left: 944px; }

  /* Page title */
  .page-title {
    position: absolute; left: 156px; top: 64px;
    display: flex; align-items: center;
  }
  .page-title__dash {
    width: 28px; height: 4px; background: var(--date-tile); margin-right: 20px; margin-top: 6px;
  }
  .page-title__text { font-size: 62px; font-weight: 300; line-height: 1; }

  /* Post list */
  .post {
    position: absolute; left: 156px; width: 860px;
    background: var(--row-gap);
  }
  .post__date {
    position: absolute; left: 0; top: 0; width: 164px; height: 78px;
    background: var(--date-tile); color: var(--date-text);
  }
  .post__day {
    position: absolute; left: 7px; top: 2px;
    font-size: 46px; font-weight: 300; line-height: 1.1;
  }
  .post__month {
    position: absolute; left: 7px; top: 55px;
    font-size: 15px; font-weight: 300; text-transform: uppercase;
  }
  .post__visual {
    position: absolute; left: 164px; top: 0; right: 0; bottom: 0;
  }
  .post__marker {
    position: absolute; left: 136px; top: 37px; width: 56px; height: 3px;
    background: #1a1a1a;
  }

  .post--1 { top: 144px; height: 78px; }
  .post--2 { top: 223px; height: 78px; }
  .post--3 { top: 303px; height: 516px; }
  .post--4 { top: 821px; height: 78px; }
  .post--5 { top: 901px; height: 78px; }
  .post--6 { top: 981px; height: 77px; }
  .post--3 .post__date { height: 75px; }

  .post--1 .post__visual { background: linear-gradient(90deg, #6e4020, #8a5228 45%, #5a3418); }
  .post--2 .post__visual { background: linear-gradient(90deg, #f0a424, #e6402e 45%, #f4a21c); }
  .post--3 .post__visual { background: radial-gradient(ellipse at 50% 30%, #4a4a4a, #1c1c1c 70%); }
  .post--4 .post__visual { background: linear-gradient(90deg, #5a5a5a, #3a3a3a 50%, #5e5e5e); }
  .post--5 .post__visual { background: linear-gradient(90deg, #5a4840, #6a4a5a 50%, #5a4840); }
  .post--6 .post__visual { background: linear-gradient(90deg, #49494b, #575759 50%, #4a4a4c); }

  /* Excerpt card */
  .post__excerpt {
    position: absolute; left: 188px; top: 294px; width: 651px; height: 214px;
    background: var(--card-bg); color: var(--card-text);
    border-left: 3px solid var(--card-border);
    padding: 20px 18px 0 19px;
  }
  .post__title { font-size: 31px; font-weight: 300; line-height: 1.2; margin-bottom: 14px; }
  .post__text { font-size: 21px; font-weight: 300; line-height: 1.3; margin-bottom: 9px; }
  .post__link { color: var(--link); text-decoration: none; }

  /* Load more */
  .load-more {
    position: absolute; left: 157px; top: 1079px; width: 859px; height: 67px;
    background: var(--load-bg); color: var(--load-text);
  }
  .load-more__label {
    position: absolute; left: 28px; top: 13px; font-size: 37px; font-weight: 300; line-height: 1.1;
  }
  .load-more__icon { position: absolute; left: 778px; top: 16px; }
</style>
</head>
<body>
  <header class="site-header">
    <div class="site-name">TWEE STILLE WERVEN</div>
    <ul class="main-nav">
      <li>HOME</li>
      <li>TWEE STILLE WERVEN</li>
      <li>ACTIVITES</li>
      <li>ABOUT US</li>
      <li>BLOG</li>
      <li>CONTACT</li>
    </ul>
    <div class="header-button header-button--top" aria-label="Back to top">
      <svg width="18" height="22" viewBox="0 0 18 22"><path d="M9 21V2M2 9l7-7 7 7" fill="none" stroke="#fff" stroke-width="1.6"/></svg>
    </div>
    <div class="header-button header-button--add" aria-label="Open menu">
      <svg width="24" height="24" viewBox="0 0 24 24"><path d="M12 1v22M1 12h22" stroke="#fff" stroke-width="1.4"/></svg>
    </div>
  </header>

  <h1 class="page-title"><span class="page-title__dash"></span><span class="page-title__text">Blog</span></h1>

  <article class="post post--1">
    <div class="post__date"><span class="post__day">16</span><span class="post__month">June 2013</span></div>
    <div class="post__visual" role="img" aria-label="Colourful illustration banner with a bird and a clock on brown wood"></div>
  </article>

  <article class="post post--2">
    <div class="post__date"><span class="post__day">19</span><span class="post__month">June 2013</span></div>
    <div class="post__visual" role="img" aria-label="Bright orange illustration banner with red bird and insect characters"></div>
  </article>

  <article class="post post--3">
    <div class="post__visual" role="img" aria-label="Dark monochrome illustration of a masked character on patterned background"></div>
    <div class="post__date"><span class="post__day">22</span><span class="post__month">May 2013</span></div>
    <span class="post__marker"></span>
    <div class="post__excerpt">
      <h2 class="post__title">Single Post on Blog</h2>
      <p class="post__text">Good luck with you project.</p>
      <p class="post__text">I'm not going to put Lorem Ipsum in here.</p>
      <p class="post__text">You can write whatever you like. <a class="post__link" href="#">Continue Reading</a>.</p>
    </div>
  </article>

  <article class="post post--4">
    <div class="post__date"><span class="post__day">5</span><span class="post__month">May 2013</span></div>
    <div class="post__visual" role="img" aria-label="Grey illustration banner with a character and large faded lettering"></div>
  </article>

  <article class="post post--5">
    <div class="post__date"><span class="post__day">24</span><span class="post__month">April 2013</span></div>
    <div class="post__visual" role="img" aria-label="Brown patterned illustration banner with colourful flowers and feathers"></div>
  </article>

  <article class="post post--6">
    <div class="post__date"><span class="post__day">11</span><span class="post__month">April 2013</span></div>
    <div class="post__visual" role="img" aria-label="Muted grey illustration banner with a small pointed shape"></div>
  </article>

  <div class="load-more">
    <span class="load-more__label">Load more</span>
    <svg class="load-more__icon" width="60" height="36" viewBox="0 0 60 36">
      <path d="M3 1v34" stroke="#e8e8e8" stroke-width="2"/>
      <path d="M33 4v28M27 25l6 7 6-7" fill="none" stroke="#e8e8e8" stroke-width="2"/>
    </svg>
  </div>
</body>
</html>
```